Business Card Design

We need a business card designed for our new company. Prefer a black card with white logo & writing.

Contact Information for Business Card

Dale Pickett, address: 7-4417 Larchmere Avenue, Abbotsford, BC, V3K 2R9, Office Phone: 604-555-0172, Cell: 604-555-0138, Email: dale@kelsoncoatworks.ca

Colors

Designer to choose only greyscale colors for use in the design.

```html
<!DOCTYPE html>
<html lang="en">
<head>
<meta charset="utf-8">
<title>Kelson Coatworks — Business Card</title>
<link href="https://fonts.googleapis.com/css2?family=Montserrat:wght@400;700&family=Lato:wght@400&display=swap" rel="stylesheet">
<style>
  :root {
    --page: #d9d9d9;
    --card: #1a1a1a;
    --ink: #ffffff;
    --ink-soft: #e6e6e6;
    --emboss: #0e0e0e;
    --rule: #cfcfcf;
  }
  * { box-sizing: border-box; margin: 0; padding: 0; }
  html, body { width: 1200px; height: 895px; overflow: hidden; }
  body {
    background: var(--page);
    display: flex; flex-direction: column; align-items: center; justify-content: center;
    gap: 40px;
  }
  .card {
    position: relative;
    width: 700px; height: 400px;
    background: var(--card);
    border-radius: 28px;
  }
  .wordmark {
    display: flex; align-items: center; gap: 12px;
    font-family: "Montserrat", sans-serif; font-weight: 700;
    text-transform: uppercase; letter-spacing: 1px; line-height: 1;
  }
  .wordmark .mark-square { width: 22px; height: 22px; background: currentColor; }

  /* back */
  .card--back .wordmark {
    position: absolute; left: 50%; top: 50%; transform: translate(-50%, -50%);
    color: var(--emboss); font-size: 44px;
  }

  /* front */
  .card--front .wordmark {
    position: absolute; right: 48px; top: 70px;
    color: var(--ink); font-size: 36px;
  }
  .divider-main {
    position: absolute; left: 250px; right: 48px; top: 180px;
    height: 1px; background: var(--rule);
  }
  .address {
    position: absolute; right: 48px; top: 200px;
    text-align: right; color: var(--ink-soft);
    font-family: "Lato", sans-serif; font-size: 19px; line-height: 1.4;
  }
  .person {
    position: absolute; left: 52px; top: 238px;
    font-family: "Montserrat", sans-serif; color: var(--ink);
  }
  .person-name { font-weight: 700; font-size: 26px; }
  .person-title { font-weight: 400; font-size: 17px; color: var(--ink-soft); margin-top: 4px; }
  .divider-small {
    position: absolute; left: 52px; top: 308px; width: 190px;
    height: 1px; background: var(--rule);
  }
  .contacts {
    position: absolute; left: 52px; top: 318px; list-style: none;
    font-family: "Lato", sans-serif; font-size: 17px; color: var(--ink-soft);
  }
  .contacts li { display: flex; align-items: center; gap: 12px; height: 23px; }
  .contacts svg { width: 16px; height: 16px; fill: var(--ink); flex: none; }
</style>
</head>
<body>
  <section class="card card--back" aria-label="Card back">
    <div class="wordmark"><span class="mark-square"></span>Kelson Coatworks</div>
  </section>

  <section class="card card--front" aria-label="Card front">
    <div class="wordmark"><span class="mark-square"></span>Kelson Coatworks</div>
    <div class="divider-main"></div>
    <address class="address" style="font-style:normal">
      7-4417 Larchmere Avenue,<br>Abbotsford, BC, V3K 2R9,
    </address>
    <div class="person">
      <p class="person-name">Dale Pickett</p>
      <p class="person-title">President</p>
    </div>
    <div class="divider-small"></div>
    <ul class="contacts">
      <li>
        <svg viewBox="0 0 16 16" aria-hidden="true"><path d="M2 5c0-2 2-3 6-3s6 1 6 3v1h-3V5H5v1H2z"/><rect x="3" y="7" width="10" height="7" rx="1"/></svg>
        604-555-0172
      </li>
      <li>
        <svg viewBox="0 0 16 16" aria-hidden="true"><path d="M5 1h6a1 1 0 0 1 1 1v12a1 1 0 0 1-1 1H5a1 1 0 0 1-1-1V2a1 1 0 0 1 1-1zm0 2v9h6V3z"/></svg>
        604-555-0138
      </li>
      <li>
        <svg viewBox="0 0 16 16" aria-hidden="true"><path d="M1 3h14v10H1zm1.5 1.2L8 8.6l5.5-4.4z"/></svg>
        dale@kelsoncoatworks.ca
      </li>
    </ul>
  </section>
</body>
</html>
```